International Trading Company, 'KIRO' needs a Business Card

The company name is "KIRO" and it has own logo design.
I'd like to use its logo on this business card.
I need two side Business Card.
I'll look forward to your great design.
Thank you very much in advance.

Contact Information for Business Card

Company Name : Kiro Harbour Limited
Information Example
Dorian Pallister
Mobile(use icon please) : 1 (212) 555-0143
Tel(use icon please) : 1 (212) 555-0178
Email(use icon please) : dorian27@kiroharbour-mail.com
Address(use icon please) : 482 Halden Ave, New York, NY 10160, USA

```html
<!DOCTYPE html>
<html lang="en">
<head>
<meta charset="utf-8">
<title>Kiro Harbour Limited – Business Card</title>
<link href="https://fonts.googleapis.com/css2?family=Noto+Sans:wght@400;700;800&display=swap" rel="stylesheet">
<style>
  :root {
    --stage: #2e2e2e;
    --card-dark: #161616;
    --card-light: #ffffff;
    --ink: #4a4a4a;
    --ink-soft: #5c5c5c;
    --mark-dark: #8c8c8c;
    --tag-dark: #3a3a3a;
    --rule: #6a6a6a;
  }
  * { margin: 0; padding: 0; box-sizing: border-box; }
  html, body {
    width: 801px; height: 1200px; overflow: hidden;
    background: var(--stage);
    font-family: "Noto Sans", Verdana, sans-serif;
  }
  .card {
    position: absolute; left: 80px;
    width: 641px; height: 366px;
    border-radius: 4px;
    box-shadow: 0 10px 30px rgba(0,0,0,.45);
  }
  .card--front { top: 117px; background: var(--card-dark); }
  .card--back  { top: 717px; background: var(--card-light); color: var(--ink); }

  .front-mark {
    position: absolute; left: 0; right: 0; top: 92px;
    text-align: center;
    font-weight: 800; font-size: 132px; line-height: 1;
    letter-spacing: -2px; color: var(--mark-dark);
  }
  .front-tagline {
    position: absolute; left: 0; right: 0; top: 245px;
    text-align: center;
    font-size: 17px; letter-spacing: 11px; color: var(--tag-dark);
  }

  .back-mark {
    position: absolute; right: 44px; top: 36px;
    font-weight: 800; font-size: 84px; line-height: 1;
    letter-spacing: -1px; color: var(--ink);
  }
  .back-tagline {
    position: absolute; right: 44px; top: 124px;
    font-size: 12px; letter-spacing: 6.5px; color: var(--ink);
  }
  .contact-person { position: absolute; left: 42px; top: 100px; }
  .person-name { font-weight: 700; font-size: 15px; letter-spacing: .4px; }
  .person-role { font-size: 15px; color: var(--ink-soft); margin-bottom: 4px; }
  .contact-line {
    display: flex; align-items: center; gap: 7px;
    font-size: 15px; line-height: 22px; color: var(--ink-soft);
  }
  .contact-line svg { width: 13px; height: 13px; fill: var(--ink); flex: none; }
  .divider {
    position: absolute; left: 340px; right: 44px; top: 208px;
    border-top: 1px solid var(--rule);
  }
  .contact-office { position: absolute; left: 340px; top: 238px; }
  .contact-office .indent { padding-left: 20px; }
</style>
</head>
<body>

<section class="card card--front" aria-label="Card front">
  <div class="front-mark">KIRO</div>
  <div class="front-tagline">KIRO HARBOUR LIMITED</div>
</section>

<section class="card card--back" aria-label="Card back">
  <div class="back-mark">KIRO</div>
  <div class="back-tagline">KIRO HARBOUR LIMITED</div>

  <div class="contact-person">
    <div class="person-name">DORIAN PALLISTER</div>
    <div class="person-role">managing director</div>
    <div class="contact-line">
      <svg viewBox="0 0 16 16" aria-hidden="true"><path d="M1 6c0-3 14-3 14 0v2h-4V6.5C9.5 6 6.5 6 5 6.5V8H1zM4 9h8l2 5H2z"/></svg>
      1 (212) 555-0178
    </div>
    <div class="contact-line">
      <svg viewBox="0 0 16 16" aria-hidden="true"><path d="M4 0h8a1 1 0 0 1 1 1v14a1 1 0 0 1-1 1H4a1 1 0 0 1-1-1V1a1 1 0 0 1 1-1zm1 2v10h6V2zm3 11a1 1 0 1 0 0 2 1 1 0 0 0 0-2z"/></svg>
      1 (212) 555-0143
    </div>
    <div class="contact-line">
      <svg viewBox="0 0 16 16" aria-hidden="true"><path d="M0 3h16v1L8 9 0 4zm0 2.5 8 5 8-5V13H0z"/></svg>
      dorian27@kiroharbour-mail.com
    </div>
  </div>

  <div class="divider"></div>

  <div class="contact-office">
    <div class="contact-line">
      <svg viewBox="0 0 16 16" aria-hidden="true"><path d="M8 0a5.5 5.5 0 0 0-5.5 5.5C2.5 10 8 16 8 16s5.5-6 5.5-10.5A5.5 5.5 0 0 0 8 0zm0 8a2.5 2.5 0 1 1 0-5 2.5 2.5 0 0 1 0 5z"/></svg>
      482 Halden Ave, New York
    </div>
    <div class="contact-line indent">NY 10160, USA</div>
    <div class="contact-line">
      <svg viewBox="0 0 16 16" aria-hidden="true"><path d="M8 0a8 8 0 1 0 0 16A8 8 0 0 0 8 0zm5.9 7h-2.5a12 12 0 0 0-1-4.6A6 6 0 0 1 13.9 7zM8 2c.8 1 1.4 2.8 1.5 5h-3C6.6 4.8 7.2 3 8 2zM5.6 2.4A12 12 0 0 0 4.6 7H2.1a6 6 0 0 1 3.5-4.6zM2.1 9h2.5a12 12 0 0 0 1 4.6A6 6 0 0 1 2.1 9zM8 14c-.8-1-1.4-2.8-1.5-5h3c-.1 2.2-.7 4-1.5 5zm2.4-.4a12 12 0 0 0 1-4.6h2.5a6 6 0 0 1-3.5 4.6z"/></svg>
      www.kiroharbour.com
    </div>
  </div>
</section>

</body>
</html>
```